IT Consulting BrightwaveTecCo.com needs Simple and Neat WebDesigns

We are a IT consulting business, currently needing a logo and a neat website that looks simple and attractive. If could be creative enough to come up with something that follows these guidelines.
We are talking about 10-15 static pages here

1. Nice and Neat
2. Color consistancy
3. Latest menu bars
4. Easy cross navigation
5. Less Maintenance
6. Easy upgrades
Updates

Project Deadline Extended
Reason: new to this and getting familiar with the time I have onhand

Project Deadline Extended

Project Deadline Extended
Reason: I want to give more time to get good quality

Project Deadline Extended

Project Deadline Extended
Reason: inviting more designs

Target Market(s)

IT services and consulting - should look very very professional and elegant.

Industry/Entity Type

Business

Requirements
Must have
• I would like to receive the best designs for our website
Nice to have
• Design a good logo to go with the website

```html
<!DOCTYPE html>
<html lang="en">
<head>
<meta charset="utf-8">
<title>BrightwaveTecCo.com</title>
<link rel="stylesheet" href="https://fonts.googleapis.com/css2?family=Arimo:ital@0;1&family=Noto+Serif:ital,wght@0,300;0,400;1,300;1,400&display=swap">
<style>
:root{
  --ink:#222;
  --bar:#000;
  --nav:#efefef;
  --nav-text:#777;
  --accent:#3b93ad;
  --teal-dark:#2b5666;
  --teal-mid:#3f7486;
  --teal-light:#6aa3b4;
  --page:#ececec;
  --rule:#c9c9c9;
  --heading:#1e4f60;
  --white:#fff;
  --hero-text:#e9f3f6;
}
*{margin:0;padding:0;box-sizing:border-box}
html,body{width:960px;height:1200px;overflow:hidden}
body{background:var(--page);font-family:"Arimo",Arial,sans-serif;color:var(--ink);position:relative}
.abs{position:absolute}
.serif{font-family:"Noto Serif",Georgia,serif;font-weight:300}

.topbar{left:0;top:0;width:960px;height:20px;background:var(--bar);color:var(--white);font-size:8.8px}
.topbar span{position:absolute;top:5px}
.topbar .support{left:420px;top:0;width:72px;height:20px;background:var(--accent);text-align:center;line-height:20px}

.mainnav{left:0;top:20px;width:960px;height:60px;background:var(--nav);border-bottom:1px solid #d6d6d6}
.mainnav a{position:absolute;top:23px;font-size:11px;color:var(--nav-text);text-decoration:none}
.mainnav .current{left:376px;top:0;width:56px;height:63px;background:linear-gradient(#4aa6c0,#2f88a3);color:var(--white);text-align:center;line-height:73px}

.hero{left:0;top:80px;width:960px;height:200px;
  background:radial-gradient(ellipse 420px 220px at 560px 110px,var(--teal-light),var(--teal-mid) 55%,var(--teal-dark));
  box-shadow:inset 0 -4px 6px rgba(0,0,0,.35)}
.slider-frame{left:80px;top:92px;width:400px;height:176px;background:#f4f4f4;padding:8px;box-shadow:0 1px 4px rgba(0,0,0,.4)}
.slider-frame .slide{width:384px;height:160px;background:linear-gradient(#3b3b3b,#1e1e1e 60%,#2a2a2a)}
.hero-title{left:492px;top:98px;font-size:18.5px;color:var(--white);font-weight:400}
.hero-text{left:492px;top:125px;width:390px;font-size:11.6px;line-height:18.4px;color:var(--hero-text)}
.hero-more{left:771px;top:248px;font-size:12.5px;font-weight:400;color:var(--white)}

.service{top:294px;width:244px;text-align:center}
.service h2{font-size:12px;font-weight:400;padding-bottom:3px;border-bottom:1px solid var(--rule);margin-bottom:6px}
.service p{font-size:9.4px;line-height:15.2px}

.divider{left:76px;width:808px;height:4px;border-radius:50%;background:#9a9a9a;box-shadow:0 2px 3px rgba(0,0,0,.3)}
.quote-band{left:0;top:442px;width:960px;height:116px;background:radial-gradient(ellipse 520px 90px at 480px 58px,#f0f0f0,#d2d2d2)}
.quote{left:80px;top:463px;width:800px;text-align:center;font-style:italic;font-size:16.4px;line-height:19.5px;color:var(--heading)}
.author{left:0;top:510px;width:960px;text-align:center;font-size:11.4px;color:var(--heading)}

.col-title{top:575px;font-size:12px;color:var(--heading);font-weight:300}
.blog{left:80px;top:595px;width:240px;list-style:none}
.blog li{height:43.2px;border-bottom:1px solid var(--rule);font-size:8.3px;line-height:10.4px}
.blog li+li{padding-top:8px}
.blog em{display:block;margin-top:4px;color:var(--heading)}
.map{left:346px;top:596px;width:240px;height:105px;background:radial-gradient(ellipse 110px 40px at 120px 50px,#555,#bbb 70%,#fff)}
.address{left:346px;top:709px;font-size:8.3px;line-height:10.4px}

.field{left:613px;width:267px;background:var(--white);border:1px solid #c4c4c4;box-shadow:inset 0 1px 2px rgba(0,0,0,.1);font-size:9.5px;font-style:italic;color:#aaa;padding:6px 8px}
.send{left:613px;top:816px;width:49px;height:24px;background:linear-gradient(#5db3cb,#2f8aa5);border:1px solid #2a7891;border-radius:2px;color:var(--white);font-size:11px;text-align:center;line-height:22px}

.partners-title{left:80px;top:861px;font-size:16.5px;font-weight:400;color:var(--heading)}
.thumb{top:888px;width:112px;height:112px;background:linear-gradient(#3a6479 0,#3a6479 18%,#b9c3c8 18%,#9aa7ae);opacity:.85}
.thumb.active{opacity:1;background:linear-gradient(#5c92b4 0,#5c92b4 18%,#f2f4f5 18%,#dde3e6)}

.footer{left:0;top:1040px;width:960px;height:160px;
  background:radial-gradient(ellipse 480px 160px at 430px 40px,#5f97a8,#3d6f81 55%,#2b5464);color:var(--white)}
.footer h3{position:absolute;top:10px;font-size:12px;font-weight:300}
.footer ul{position:absolute;top:28px;width:240px;list-style:none}
.footer li{height:20.8px;font-size:8.6px;line-height:16px;border-bottom:1px solid rgba(255,255,255,.15)}
.footer li:last-child{border-bottom:none}
.footer .vline{position:absolute;left:613px;top:8px;width:1px;height:145px;background:rgba(255,255,255,.2)}
.footer .legal{position:absolute;left:623px;font-size:8.6px}
</style>
</head>
<body>

<div class="abs topbar">
  <span style="left:80px">Welcome to BrightwaveTecCo.com!</span>
  <span style="left:294px">Call us at: 123 456 789</span>
  <span class="support">Live support!</span>
</div>

<nav class="abs mainnav">
  <a class="current" href="#" style="line-height:73px">Home</a>
  <a href="#" style="left:449px">About Us</a>
  <a href="#" style="left:524px">Services</a>
  <a href="#" style="left:595px">Portfolio</a>
  <a href="#" style="left:665px">Contact Us</a>
  <a href="#" style="left:749px">Blog</a>
</nav>

<section class="abs hero"></section>
<div class="abs slider-frame"><div class="slide" role="img" aria-label="Portfolio slideshow with a dark wooden backdrop and a green welcome caption"></div></div>
<h1 class="abs serif hero-title">Welcome to BrightwaveTecCo.com!</h1>
<p class="abs serif hero-text">Pellentesque habitant morbi tristique senectus et netus et malesuada fames ac turpis egestas. Phasellus magna turpis, dignissim eu venenatis ac, ultricies eget sem. Sed eget diam at ante pretium mollis eu in lacus. Curabitur nulla turpis, faucibus in scelerisque nec, condimentum sit amet eros. Donec pulvinar ultricies ante, sit amet commodo purus congue sit amet. Duis rhoncus lectus et urna egestas id varius lorem condimentum.</p>
<div class="abs serif hero-more">Read more!</div>

<div class="abs service" style="left:91px"><h2 class="serif">Web Design</h2><p>Pellentesque habitant morbi tristique senectus et netus et malesuada fames ac turpis egestas. Phasellus magna turpis, dignissim eu venenatis ac, ultricies eget sem. Sed eget diam at ante pretium mollis eu in lacus. Curabitur nulla turpis, faucibus in scelerisque nec, condimentum sit amet eros.</p></div>
<div class="abs service" style="left:358px"><h2 class="serif">Web Development</h2><p>Morbi varius augue sed orci mollis sed aliquam urna pellentesque. Phasellus ornare faucibus est, vel posuere urna interdum ut. In hac habitasse platea dictumst. Class aptent taciti sociosqu ad litora torquent per conubia nostra, per inceptos himenaeos. Etiam semper pretium imperdiet.</p></div>
<div class="abs service" style="left:624px"><h2 class="serif">SEO &amp; Advertising Campaigns</h2><p>Nunc consectetur pulvinar volutpat. Praesent sed mi arcu. Quisque at tortor eu velit imperdiet ultrices. Vivamus sit amet enim nec velit bibendum interdum sed et ipsum. Donec laoreet est nibh. Sed felis mauris, tristique mollis ultrices non, mollis non tellus.</p></div>

<div class="abs quote-band"></div>
<div class="abs divider" style="top:438px"></div>
<blockquote class="abs serif quote">"Vivamus sit amet urna eget velit pharetra luctus. Quisque in tortor facilisis dolor sagittis mattis. In suscipit gravida eros, eleifend convallis elit congue ultricies."</blockquote>
<div class="abs serif author">Mr. Businessman - Entrepreneur</div>
<div class="abs divider" style="top:556px"></div>

<h2 class="abs serif col-title" style="left:80px">Recent From Blog</h2>
<ul class="abs blog">
  <li>Cras malesuada, risus ac faucibus congue, purus nunc dictum purus, in molestie magna nunc sit amet ligula.<em>Read more...</em></li>
  <li>Cras malesuada, risus ac faucibus congue, purus nunc dictum purus, in molestie magna nunc sit amet ligula.<em>Read more...</em></li>
  <li>Cras malesuada, risus ac faucibus congue, purus nunc dictum purus, in molestie magna nunc sit amet ligula.<em>Read more...</em></li>
  <li>Cras malesuada, risus ac faucibus congue, purus nunc dictum purus, in molestie magna nunc sit amet ligula.<em>Read more...</em></li>
  <li>Cras malesuada, risus ac faucibus congue, purus nunc dictum purus, in molestie magna nunc sit amet ligula.<em>Read more...</em></li>
</ul>

<h2 class="abs serif col-title" style="left:346px">Location</h2>
<div class="abs map" role="img" aria-label="World map showing the office location"></div>
<div class="abs address">Country<br>State/Province<br>Address<br><br>Phone: 123 456 789<br>Fax: 123 456 789<br>Email: contact@brightwavetecco.com</div>

<h2 class="abs serif col-title" style="left:613px">Contact Us</h2>
<div class="abs field" style="top:596px;height:23px">Your name...</div>
<div class="abs field" style="top:632px;height:23px">Your email...</div>
<div class="abs field" style="top:668px;height:140px">Your message...</div>
<div class="abs send">Send</div>

<div class="abs divider" style="top:854px"></div>
<h2 class="abs serif partners-title">Partners and Projects</h2>
<div class="abs thumb" style="left:80px" role="img" aria-label="Partner website preview"></div>
<div class="abs thumb active" style="left:219px" role="img" aria-label="Partner website preview"></div>
<div class="abs thumb" style="left:351px" role="img" aria-label="Partner website preview"></div>
<div class="abs thumb" style="left:491px" role="img" aria-label="Partner website preview"></div>
<div class="abs thumb" style="left:630px" role="img" aria-label="Partner website preview"></div>
<div class="abs thumb" style="left:768px" role="img" aria-label="Partner website preview"></div>
<div class="abs divider" style="top:1012px"></div>

<footer class="abs footer">
  <h3 class="serif" style="left:80px">Main Navigation</h3>
  <ul style="left:80px"><li>Home</li><li>About Us</li><li>Services</li><li>Portfolio</li><li>Contact Us</li><li>Blog</li></ul>
  <h3 class="serif" style="left:346px">Our Services</h3>
  <ul style="left:346px"><li>Web Design</li><li>Web Development</li><li>Software Development</li><li>SEO</li><li>Advertising Campaigns</li></ul>
  <div class="vline"></div>
  <div class="legal" style="top:10px">© 2011 BrightwaveTecCo.com</div>
  <div class="legal" style="top:31px">Privacy Policy | Terms and Conditions</div>
  <div class="legal" style="top:52px">Follow us on: &nbsp;&nbsp;&nbsp; Linkwave &nbsp; | &nbsp; ArtCircle &nbsp; | &nbsp; Chirper</div>
</footer>

</body>
</html>
```